Torvane Systems*

Stationary design including business cards, letter heads, envelops and email signatures using our new logo

Target Market(s)

Innovative Technologies

Industry/Entity Type

Defense Contracting

Font styles to use
Sans Serif

```html
<!DOCTYPE html>
<html lang="en">
<head>
<meta charset="utf-8">
<title>Torvane Systems Stationery</title>
<link href="https://fonts.googleapis.com/css2?family=Barlow:wght@400;600&family=Barlow+Condensed:wght@400;600&family=Arimo:wght@400&display=swap" rel="stylesheet">
<style>
:root{
  --board:#7b7b7b;
  --paper:#ffffff;
  --ink:#1c1c1e;
  --text:#2a2a2a;
  --muted:#555;
  --light:#f2f2f2;
}
*{box-sizing:border-box;margin:0;padding:0}
html,body{width:1200px;height:699px;overflow:hidden}
body{background:var(--board);position:relative;font-family:'Barlow',sans-serif;color:var(--text)}
.sheet{position:absolute;background:var(--paper);overflow:hidden}
.band{position:absolute;left:0;right:0;background:var(--ink);color:#fff}
.wordmark{font-family:'Barlow Condensed',sans-serif;font-weight:400;color:var(--ink);white-space:nowrap;letter-spacing:.2px}
.wordmark.light{color:#fff}
.mark-square{display:inline-block;border:1px solid currentColor;vertical-align:middle;margin-right:4px}
.contact{font-size:6px;line-height:7px}
.contact li{list-style:none;display:flex;align-items:center;gap:3px}
.ico{width:5px;height:5px;flex:none;fill:currentColor}

/* letterhead */
.letterhead{left:344px;top:59px;width:406px;height:573px}
.letterhead .band{top:42px;height:41px}
.letterhead .company{position:absolute;right:118px;top:11px;text-align:right;font-size:6.4px;line-height:8px}
.letterhead .divider{position:absolute;right:112px;top:10px;width:1px;height:24px;background:#fff}
.letterhead .contact{position:absolute;left:300px;top:11px;font-size:6.4px;line-height:8px}
.letterhead .brand{position:absolute;left:33px;top:91px;font-size:14px}
.letter{position:absolute;left:34px;top:160px;width:340px;font-family:'Arimo',sans-serif}
.letter .salute{font-size:9px;color:#444;margin-bottom:16px}
.letter p{font-size:5.2px;line-height:8.2px;color:#555;margin-bottom:8.4px;text-align:justify}
.letter .close{margin-top:14px}
.signature{position:absolute;left:30px;top:389px;width:108px;height:26px;background:linear-gradient(90deg,#eee,#f7f7f7)}

/* business card */
.card-front{left:72px;top:320px;width:243px;height:138px}
.card-front .band{top:19px;height:40px}
.card-front .name{position:absolute;left:13px;top:14px;font-family:'Barlow Condensed',sans-serif;font-weight:600;font-size:9px}
.card-front .role{position:absolute;left:13px;top:24px;font-size:5.4px}
.card-front .brand{position:absolute;right:15px;top:63px;font-size:14px}
.card-front .contact{position:absolute;left:13px;top:104px}
.card-front .address{position:absolute;right:15px;top:104px;text-align:right;font-size:5.6px;line-height:6.6px}
.card-front .address b{font-weight:600}
.card-back{left:72px;top:494px;width:243px;height:138px;background:var(--ink);display:flex;align-items:center;justify-content:center}
.card-back .wordmark{font-size:16px}

/* email signature */
.email-sig{left:782px;top:194px;width:333px;height:85px}
.email-sig .brand{position:absolute;left:18px;top:58px;font-size:10px}
.email-sig .rule{position:absolute;top:23px;width:1px;height:41px;background:var(--ink)}
.email-sig .person{position:absolute;left:110px;top:20px;font-size:6.4px;line-height:8px}
.email-sig .person .name{font-family:'Barlow Condensed',sans-serif;font-weight:600;font-size:10.5px;line-height:11px;color:var(--ink)}
.email-sig .contact{position:absolute;left:236px;top:24px;font-size:6.2px;line-height:7.8px}

/* envelopes */
.envelope-back{left:783px;top:308px;width:330px;height:147px;background:var(--paper)}
.envelope-back svg{position:absolute;inset:0}
.envelope-back .wordmark{position:absolute;left:0;right:0;top:40px;text-align:center;font-size:11px}
.envelope-front{left:780px;top:485px;width:333px;height:149px}
.envelope-front .band{top:17px;height:30px}
.envelope-front .address{position:absolute;left:64px;top:8px;font-size:6.2px;line-height:8px}
.envelope-front .brand{position:absolute;left:17px;top:53px;font-size:10px}
</style>
</head>
<body>

<!-- Business card front -->
<section class="sheet card-front" aria-label="Business card front">
  <div class="band">
    <div class="name">DANIEL REYES</div>
    <div class="role">President</div>
  </div>
  <div class="wordmark brand">Torvane Systems</div>
  <ul class="contact">
    <li><svg class="ico" viewBox="0 0 10 10"><path d="M2 0l2 2-1 2 3 3 2-1 2 2-2 2C4 10 0 6 0 2z"/></svg>555-214-7730</li>
    <li><svg class="ico" viewBox="0 0 10 10"><path d="M2 0h6v10H2zM3 1v7h4V1z"/></svg>555-308-6142</li>
    <li><svg class="ico" viewBox="0 0 10 10"><path d="M0 2h10v6H0zM0 2l5 3 5-3"/></svg>info@torvanesys.com</li>
  </ul>
  <div class="address"><b>Torvane Systems LLC</b><br>4120 Birchwood Court, Fairbanks, Alaska 99701<br>www.torvanesys.com</div>
</section>

<!-- Business card back -->
<section class="sheet card-back" aria-label="Business card back">
  <div class="wordmark light">Torvane Systems</div>
</section>

<!-- Letterhead -->
<section class="sheet letterhead" aria-label="Letterhead">
  <div class="band">
    <div class="company">Torvane Systems LLC<br>4120 Birchwood Court, Fairbanks, Alaska 99701<br>www.torvanesys.com</div>
    <div class="divider"></div>
    <ul class="contact">
      <li><svg class="ico" viewBox="0 0 10 10"><path d="M2 0l2 2-1 2 3 3 2-1 2 2-2 2C4 10 0 6 0 2z"/></svg>555-214-7730</li>
      <li><svg class="ico" viewBox="0 0 10 10"><path d="M2 0h6v10H2zM3 1v7h4V1z"/></svg>555-308-6142</li>
      <li><svg class="ico" viewBox="0 0 10 10"><path d="M0 2h10v6H0z"/></svg>info@torvanesys.com</li>
    </ul>
  </div>
  <div class="wordmark brand">Torvane Systems</div>
  <div class="letter">
    <div class="salute">Dear Mr. Reyes,</div>
    <p>Lorem ipsum dolor sit amet, consectetur adipiscing elit. Donec orci purus, luctus vitae dignissim eu, iaculis sed purus. Vivamus faucibus, ipsum nec aliquet viverra, leo mauris condimentum ligula, sit amet sagittis enim ligula quis arcu. Nam egestas tortor id nisi porttitor mattis. In tortor ante, ultricies in suscipit a, tempus non massa. Vivamus et auctor mi. Fusce vel massa nulla. Phasellus nec eros mauris, et scelerisque orci.</p>
    <p>Donec malesuada orci vitae nulla accumsan porta a id massa. Quisque accumsan iaculis magna sit amet fringilla. Maecenas consequat, magna eget tincidunt semper, odio nibh rutrum mi, id feugiat ante nisi eu risus. Vestibulum nunc orci, rhoncus a placerat in, ultricies in mi. Cras mattis varius eros, vel fringilla nisi suscipit eget. Quisque scelerisque sagittis nulla at porttitor.</p>
    <p>Sed id augue vitae urna euismod commodo aliquet a quam. Pellentesque arcu velit, cursus et malesuada ut, consequat et diam. Nullam erat sem, rhoncus id ullamcorper vitae, rhoncus et arcu. In ultricies ultricies nulla, ut rutrum nisi iaculis at. Donec eu magna a metus ornare faucibus. Fusce aliquet faucibus ultricies. Morbi semper, est id tincidunt gravida, sem arcu adipiscing lacus, ac bibendum nulla leo eu purus. Quisque nec diam sed risus consectetur accumsan quis quis nibh. Vestibulum id purus lorem.</p>
    <p>It is a long established fact that a reader will be distracted by the readable content of a page when looking at its layout. The point of using Lorem Ipsum is that it has a more-or-less normal distribution of letters, as opposed to using 'Content here, content here', making it look like readable English. Many desktop publishing packages</p>
    <p>ada ut, consequat et diam. Nullam erat sem, rhoncus id ullamcorper vitae, rhoncus et arcu. In ultricies ultricies nulla, ut rutrum nisi iaculis at. Donec eu magna a metus ornare faucibus. Fusce aliquet faucibus ultricies. Morbi semper,</p>
    <p class="close">Sincerely,</p>
  </div>
  <div class="signature" role="img" aria-label="Handwritten signature"></div>
</section>

<!-- Email signature -->
<section class="sheet email-sig" aria-label="Email signature">
  <div class="wordmark brand">Torvane Systems</div>
  <div class="rule" style="left:89px"></div>
  <div class="person">
    <div class="name">DANIEL REYES</div>
    President<br>
    <span style="color:var(--ink);font-weight:600">Torvane Systems LLC</span><br>
    4120 Birchwood Court<br>
    Fairbanks, Alaska 99701
  </div>
  <div class="rule" style="left:216px"></div>
  <ul class="contact">
    <li><svg class="ico" viewBox="0 0 10 10"><path d="M2 0l2 2-1 2 3 3 2-1 2 2-2 2C4 10 0 6 0 2z"/></svg>555-214-7730</li>
    <li><svg class="ico" viewBox="0 0 10 10"><path d="M2 0h6v10H2zM3 1v7h4V1z"/></svg>555-308-6142</li>
    <li><svg class="ico" viewBox="0 0 10 10"><path d="M2 0h6v3h2v5H0V3h2z"/></svg>555-417-2095</li>
    <li><svg class="ico" viewBox="0 0 10 10"><path d="M0 2h10v6H0z"/></svg>info@torvanesys.com</li>
    <li><svg class="ico" viewBox="0 0 10 10"><circle cx="5" cy="5" r="5"/></svg>www.torvanesys.com</li>
  </ul>
</section>

<!-- Envelope back -->
<section class="sheet envelope-back" aria-label="Envelope back">
  <svg viewBox="0 0 330 147" preserveAspectRatio="none">
    <path d="M0 147L112 72M330 147L226 72" stroke="#e6e6e6" stroke-width="1" fill="none"/>
    <path d="M0 0H330Q326 10 318 14L190 82Q165 96 140 82L12 14Q4 10 0 0Z" fill="#1c1c1e"/>
  </svg>
  <div class="wordmark light">Torvane Systems</div>
</section>

<!-- Envelope front -->
<section class="sheet envelope-front" aria-label="Envelope front">
  <div class="band">
    <div class="address">Torvane Systems LLC<br>4120 Birchwood Court, Fairbanks, Alaska 99701</div>
  </div>
  <div class="wordmark brand">Torvane Systems</div>
</section>

</body>
</html>
```